Brom-leigh Sky Harbour Custom Brokers Limited

Shop online from the USA and Ship to Jamaica
Customs Brokerage, Import Export and logistic Services
Address:- 238-240 Halden Brook Road Kingston Jamaica
Email: info@bromleighskyharbour,com
Web: www.bromleighskyharbour.com
Telephone: (876) 555-0148, (876) 555-0193
flyer should be quarter page must print information on back and front

```html
<!DOCTYPE html>
<html lang="en">
<head>
<meta charset="utf-8">
<title>Brom-leigh Sky Harbour Custom Brokers – Flyer</title>
<link rel="stylesheet" href="https://fonts.googleapis.com/css2?family=Oswald:wght@400;500&family=Open+Sans:wght@400;600&display=swap">
<style>
  :root {
    --brand-red: #e2362c;
    --band-red: rgba(226, 54, 44, 0.9);
    --navy: #1e2f57;
    --navy-band: rgba(24, 40, 78, 0.92);
    --container-green: #3f8a6b;
    --container-green-dark: #2f7457;
    --circle-grey: rgba(222, 226, 222, 0.88);
    --white: #ffffff;
    --sky: #4f7fbf;
    --container-red: #b8302c;
  }
  * { box-sizing: border-box; margin: 0; padding: 0; }
  html, body { width: 1200px; height: 887px; overflow: hidden; background: #fff; }
  .flyer { position: relative; width: 1200px; height: 887px; overflow: hidden; font-family: "Open Sans", sans-serif; }

  /* Front panel */
  .front { position: absolute; left: 0; top: 0; width: 597px; height: 887px; overflow: hidden; }
  .front-photo {
    position: absolute; inset: 0;
    background: linear-gradient(170deg, var(--sky) 0%, #7d93b8 14%, #a84a4a 30%, var(--container-red) 55%, #a9372f 78%, #8d3a36 100%);
  }
  .brand-name {
    position: absolute; left: 28px; top: 62px;
    color: var(--navy); font-weight: 600; font-size: 19px; line-height: 1.25; letter-spacing: 0.5px;
  }
  .brand-name .brand-sub { display: block; font-size: 11px; letter-spacing: 4px; }
  .title-band {
    position: absolute; left: 0; top: 241px; width: 597px; height: 155px;
    background: var(--band-red); text-align: center; color: var(--white);
  }
  .title-band h1 { font-family: "Oswald", sans-serif; font-weight: 500; font-size: 56px; line-height: 1; margin-top: 22px; letter-spacing: -0.5px; }
  .title-band p { font-size: 31px; margin-top: 12px; letter-spacing: -0.3px; white-space: nowrap; }
  .front-graphics { position: absolute; left: 0; top: 0; }
  .tagline-band {
    position: absolute; left: 0; top: 822px; width: 597px; height: 30px;
    background: var(--navy-band); color: var(--white); text-align: center;
    font-size: 24px; line-height: 30px; white-space: nowrap;
  }

  /* Back panel */
  .back {
    position: absolute; left: 597px; top: 0; width: 603px; height: 887px;
    background: linear-gradient(90deg, var(--container-green) 0%, var(--container-green-dark) 20%, var(--container-green) 40%, var(--container-green-dark) 60%, var(--container-green) 80%, var(--container-green-dark) 100%);
  }
  .info-circle {
    position: absolute; left: 11px; top: 132px; width: 582px; height: 582px;
    border-radius: 50%; background: var(--circle-grey);
  }
  .info-heading {
    position: absolute; left: 0; top: 328px; width: 612px; text-align: center;
    font-family: "Oswald", sans-serif; font-weight: 400; font-size: 34px; line-height: 44px;
    color: var(--brand-red); white-space: nowrap;
    transform: scaleX(0.74); transform-origin: center;
  }
  .contact-list { position: absolute; left: 40px; top: 383px; list-style: none; }
  .contact-list li {
    position: relative; padding-left: 19px; font-size: 19.5px; color: var(--navy);
    height: 39px; line-height: 26px; white-space: nowrap; letter-spacing: -0.2px;
  }
  .contact-list li::before {
    content: ""; position: absolute; left: 0; top: 7px; width: 12px; height: 12px;
    border-radius: 50%; background: var(--brand-red);
  }
</style>
</head>
<body>
<main class="flyer">
  <section class="front">
    <div class="front-photo" role="img" aria-label="Photo: stacked red and grey shipping containers under a blue sky, a man in a blue sweater looking up at them"></div>

    <div class="brand-name">Brom-leigh Sky Harbour<span class="brand-sub">Custom Brokers Ltd.</span></div>

    <div class="title-band">
      <h1>Customs Brokerage</h1>
      <p>Import Export and logistic Services</p>
    </div>

    <svg class="front-graphics" width="597" height="887" viewBox="0 0 597 887">
      <defs>
        <linearGradient id="arrowSky" x1="0" y1="0" x2="1" y2="0">
          <stop offset="0" stop-color="#7aa6d8"/>
          <stop offset="1" stop-color="#b9d3ec"/>
        </linearGradient>
        <radialGradient id="lagoon" cx="0.5" cy="0.5" r="0.5">
          <stop offset="0" stop-color="#2f8f8a"/>
          <stop offset="1" stop-color="#145a5c"/>
        </radialGradient>
      </defs>
      <path role="img" aria-label="Photo: Statue of Liberty against a cloudy sky inside a curved arrow"
            d="M24 541 C120 455 220 420 300 428 L262 384 L399 466 L296 540 L301 492 C220 486 130 520 52 600 Z"
            fill="url(#arrowSky)" stroke="var(--white)" stroke-width="4" stroke-linejoin="round"/>
      <circle role="img" aria-label="Aerial photo: overwater villas arranged in a heart shape on a turquoise lagoon"
              cx="486" cy="526" r="89" fill="url(#lagoon)" stroke="var(--white)" stroke-width="4"/>
    </svg>

    <div class="tagline-band">Shop online from the USA and Ship to Jamaica</div>
  </section>

  <section class="back">
    <div class="info-circle"></div>
    <h2 class="info-heading">Shop online from the USA and Ship to Jamaica</h2>
    <ul class="contact-list">
      <li>Address:- 238-240 Halden Brook Road Kingston Jamaica</li>
      <li>Email: info@bromleighskyharbour,com</li>
      <li>Web: www.bromleighskyharbour.com</li>
      <li>Telephone: (876) 555-0148, (876) 555-0193</li>
    </ul>
  </section>
</main>
</body>
</html>
```